Creative Design "Size Chart" for a Clothing Product

Hi, My dear friends! I am looking to do a contest to design a unique creative "Size Chart" for our clothing line. See Attached the Sizes & Ideas Thanks Good Luck Dorian

Colors

Designer to choose colors to be used in the design.

```html
<!DOCTYPE html>
<html lang="en">
<head>
<meta charset="utf-8">
<title>Size Chart</title>
<link rel="stylesheet" href="https://fonts.googleapis.com/css2?family=Rajdhani:wght@400;500;700&display=swap">
<style>
  :root {
    --bg: #ffffff;
    --ink: #111111;
    --figure-top: #ee1e57;
    --figure-mid: #f3828f;
    --figure-low: #f5a3ac;
    --header: #f05d70;
    --header-text: #ffffff;
    --row-1: #f7b4b4;
    --row-2: #f9bfbe;
    --row-3: #f9c7c6;
    --row-4: #fbd3d2;
    --row-5: #fcdcd9;
    --row-6: #fde7e3;
    --row-7: #fef1ef;
    --dash: #fbd0d6;
  }
  * { margin: 0; padding: 0; box-sizing: border-box; }
  html, body { width: 1200px; height: 1200px; overflow: hidden; background: var(--bg); }
  .size-chart {
    position: relative;
    width: 1200px;
    height: 1200px;
    font-family: "Rajdhani", sans-serif;
    color: var(--ink);
  }
  .figure-area {
    position: absolute;
    left: 469px;
    top: 90px;
    width: 262px;
    height: 556px;
    border-radius: 120px 120px 0 0;
    background: linear-gradient(to bottom,
      var(--figure-top) 0%,
      var(--figure-mid) 45%,
      var(--figure-low) 78%,
      rgba(255,255,255,0) 100%);
  }
  .measure-marks {
    position: absolute;
    left: 0;
    top: 0;
    width: 1200px;
    height: 700px;
    pointer-events: none;
  }
  .measure-label {
    font-family: "Rajdhani", sans-serif;
    font-weight: 700;
    font-size: 28px;
    fill: #ffffff;
  }
  .chart-table {
    position: absolute;
    left: 90px;
    top: 649px;
    width: 1020px;
  }
  .chart-row {
    display: grid;
    grid-template-columns: 340px 340px 340px;
    align-items: center;
    height: 57.6px;
  }
  .chart-head {
    height: 58px;
    background: var(--header);
    color: var(--header-text);
    font-weight: 700;
    font-size: 32px;
    text-align: center;
  }
  .chart-head .col-size { text-align: center; }
  .col-size { padding-left: 47px; font-weight: 700; font-size: 31px; }
  .col-chest, .col-waist { text-align: center; font-weight: 400; font-size: 31px; letter-spacing: 1px; }
  .col-waist { padding-left: 0; transform: translateX(0); }
  .chart-row .col-chest { margin-left: 0; }
  .chart-row .col-waist { margin-left: 0; }
  .chart-row.compact .col-size,
  .chart-row.compact .col-chest,
  .chart-row.compact .col-waist { font-size: 24px; }
  .row-xs { background: var(--row-1); }
  .row-s  { background: var(--row-2); }
  .row-m  { background: var(--row-3); }
  .row-l  { background: var(--row-4); }
  .row-xl { background: var(--row-5); }
  .row-2x { background: var(--row-6); }
  .row-3x { background: var(--row-7); }
</style>
</head>
<body>
<main class="size-chart">
  <div class="figure-area" role="img" aria-label="Silhouette of a woman's upper body showing where chest and waist are measured"></div>

  <svg class="measure-marks" viewBox="0 0 1200 700" aria-hidden="true">
    <ellipse cx="600" cy="337" rx="72" ry="22" fill="none" stroke="var(--dash)" stroke-width="2" stroke-dasharray="6 4"/>
    <text class="measure-label" x="600" y="347" text-anchor="middle">CHEST</text>
    <ellipse cx="600" cy="441" rx="59" ry="22" fill="none" stroke="var(--dash)" stroke-width="2" stroke-dasharray="6 4"/>
    <text class="measure-label" x="600" y="451" text-anchor="middle">WAIST</text>
  </svg>

  <section class="chart-table">
    <div class="chart-row chart-head">
      <span class="col-size">SIZE</span>
      <span class="col-chest">CHEST</span>
      <span class="col-waist">WAIST</span>
    </div>
    <div class="chart-row row-xs"><span class="col-size">XS (0-2)</span><span class="col-chest">32-34</span><span class="col-waist">26-28</span></div>
    <div class="chart-row row-s"><span class="col-size">S (4-6)</span><span class="col-chest">34-36</span><span class="col-waist">28-30</span></div>
    <div class="chart-row row-m compact"><span class="col-size">M (8-10)</span><span class="col-chest">36-38</span><span class="col-waist">30-32</span></div>
    <div class="chart-row row-l"><span class="col-size">L (12-14)</span><span class="col-chest">38-40</span><span class="col-waist">32-34</span></div>
    <div class="chart-row row-xl"><span class="col-size">XL (14-16)</span><span class="col-chest">40-42</span><span class="col-waist">34-36</span></div>
    <div class="chart-row row-2x"><span class="col-size">2X (18)</span><span class="col-chest">42-44</span><span class="col-waist">36-38</span></div>
    <div class="chart-row row-3x"><span class="col-size">3X (20)</span><span class="col-chest">44-46</span><span class="col-waist">38-40</span></div>
  </section>
</main>
</body>
</html>
```